Cyber Security firm working in the Financial Services sector needs a brochure

We need a brochure covering our products and offerings. We work exclusively with Independent Broker Dealers, their Reps and RIAs in the US. We help them keep their computers secure and compliant with applicable regulations and policies. Have attached samples of our logo an descriptions of our products and services.

Target Market(s)

Financial Institutions and Financial Advisors

Industry/Entity Type

Financial Service

```html
<!DOCTYPE html>
<html lang="en">
<head>
<meta charset="utf-8">
<title>Keystone Shield – Services Brochure</title>
<link rel="stylesheet" href="https://fonts.googleapis.com/css2?family=Arimo:wght@400;700&family=Roboto+Condensed:wght@400;700&display=swap">
<style>
:root{
  --bg:#e6e6e6;
  --paper:#ffffff;
  --royal:#2546a6;
  --head-blue:#2c4fa8;
  --ink:#2b2b2b;
  --footer:#2a2c30;
  --footer-text:#c9ccd1;
}
*{box-sizing:border-box;margin:0;padding:0}
html,body{width:1200px;height:1200px;overflow:hidden;background:var(--bg)}
body{position:relative;font-family:"Roboto Condensed","Arial Narrow",sans-serif;color:var(--ink)}
.page{position:absolute;background:var(--paper);overflow:hidden;box-shadow:0 4px 10px rgba(0,0,0,.25)}
.page--front{left:12px;top:20px;width:572px;height:738px}
.page--back{left:612px;top:355px;width:568px;height:734px}
.photo{position:absolute}
.body-text{font-size:8.4px;line-height:11.1px;text-align:justify}
.section-title{font-family:"Arimo",Arial,sans-serif;font-weight:700;font-size:11.2px;color:var(--head-blue);margin:10px 0 6px}

/* front page */
.front-photo-meeting{left:0;top:0;width:284px;height:192px;background:linear-gradient(135deg,#d9dde2 0%,#f1f1f1 40%,#5a5f66 75%,#2c2f35 100%)}
.intro-panel{position:absolute;left:0;top:192px;width:284px;height:484px;background:var(--royal);color:#fff}
.brand-name{position:absolute;left:70px;top:28px;font-family:"Arimo",Arial,sans-serif;font-weight:700;font-size:23px;line-height:27px;color:#fff}
.brand-name .dot{display:inline-block;width:9px;height:9px;border-radius:50%;background:#fff;margin-right:6px;vertical-align:middle}
.intro-copy{position:absolute;left:26px;right:12px;top:126px;font-family:"Arimo",Arial,sans-serif;font-size:11px;line-height:13.5px;text-align:justify}
.intro-copy p{margin-bottom:13px}
.intro-copy .lead-in{display:flex;align-items:center;gap:4px}
.panel-services{position:absolute;left:12px;right:12px;top:306px}
.panel-services .section-title{color:#fff;margin-top:8px}
.panel-services .body-text{color:#e6ecff}
.front-column{position:absolute;left:300px;top:30px;width:259px}
.front-photo-tablet{left:289px;top:524px;width:281px;height:150px;background:linear-gradient(120deg,#6d5a48 0%,#c9b49a 40%,#3b3a3d 70%,#8c8e93 100%)}
.contact-bar{position:absolute;left:0;top:676px;width:572px;height:62px;background:var(--footer);color:var(--footer-text)}
.contact-photo{left:0;top:0;width:104px;height:62px;background:linear-gradient(135deg,#8a6a58,#d8c3b4 55%,#5e5e62)}
.company-block{position:absolute;left:138px;top:11px;font-family:"Arimo",Arial,sans-serif;font-size:10px;line-height:13px}
.company-block strong{display:block;font-size:13px;line-height:16px;color:#e7e9ec;font-weight:700}
.reach-block{position:absolute;left:342px;top:19px;font-family:"Arimo",Arial,sans-serif;font-size:10.4px;line-height:17px}

/* back page */
.back-photo-growth{left:0;top:0;width:568px;height:157px;background:linear-gradient(100deg,#f1f7fb 0%,#cfe6f5 35%,#4ca0d8 70%,#1f6cb4 100%)}
.config-column{position:absolute;left:14px;top:167px;width:254px}
.config-column .section-title{margin:0 0 8px}
.config-column .subhead{font-family:"Arimo",Arial,sans-serif;font-size:9px;color:var(--head-blue);margin:10px 0 2px}
.config-column ul{list-style:none}
.config-column li{font-size:8.4px;line-height:11.1px;padding-left:18px;position:relative}
.config-column li::before{content:"";position:absolute;left:8px;top:4px;width:3.5px;height:3.5px;border-radius:50%;background:var(--ink)}
.config-column li small{font-size:5.6px}
.back-photo-trading{left:0;top:457px;width:276px;height:156px;background:linear-gradient(135deg,#3b4f69 0%,#1c2534 50%,#f2f2f2 85%,#dcdcdc 100%)}
.back-photo-tablet{left:0;top:613px;width:276px;height:121px;background:linear-gradient(110deg,#eef0f2 0%,#c7cdd3 40%,#5d4c3f 70%,#d8dde2 100%)}
.service-box{position:absolute;left:278px;width:290px;padding:6px 10px 0 10px;color:#fff}
.service-box .section-title{color:#fff;margin:0 0 8px}
.service-box .body-text{color:#eef5ff}
.service-box .body-text + .body-text{margin-top:11px}
.box-support{top:162px;height:119px;background:#2d9bd9}
.box-awareness{top:283px;height:174px;background:#2a86cf}
.box-filtering{top:459px;height:107px;background:#2a6fc2}
.box-firewall{top:568px;height:82px;background:#2a5cb5}
.box-ip{top:652px;height:82px;background:#2a4ea8}
</style>
</head>
<body>

<article class="page page--front">
  <div class="photo front-photo-meeting" role="img" aria-label="Photo of an advisor meeting with clients at a desk with laptop and reports"></div>

  <section class="intro-panel">
    <div class="brand-name"><span class="dot"></span>Keystone<br>Shield</div>
    <div class="intro-copy">
      <p>Keystone Shield provides Computer Security support and services to the Broker Dealer and Independent Advisor community.</p>
      <p>We have been providing these services for over eight years and our team has decades of experience in the Financial Services sector. We currently support, monitor and inspect thousands of Advisors and their devices across multiple Broker Dealers and RIAs.</p>
      <p class="lead-in">Below is a list of our most popular services.
        <svg width="10" height="14" viewBox="0 0 10 14"><path d="M2 1 Q9 7 2 13" fill="none" stroke="#fff" stroke-width="2"/></svg></p>
    </div>
    <div class="panel-services">
      <h2 class="section-title">Managed Backup</h2>
      <p class="body-text">We partner with Northline owned Arcvault Pro to provide backup services. This provides encrypted transmission and storage in SSAE 16 audited and ISO 27001 certified facilities for your back-up needs. We help you configure the back-ups, monitor them on a daily basis and are are there to help if you need to do any restores. Price $1 per GB per month.</p>
      <h2 class="section-title">Managed Anti-Virus</h2>
      <p class="body-text">Correctly functioning and up-to-date Anti-Virus (AV) software is a requirement for all computers connected to the internet. With only one or two computers it is relatively easy to stay on top of the situation. However, once you get more than a couple of computers and users knowing their condition becomes more difficult without centralized reporting and monitoring.</p>
    </div>
  </section>

  <section class="front-column">
    <p class="body-text">Our managed AV solution provides a centralized portal for monitoring and reporting. We are notified of any issues, whether it's a virus detected or an issue with the AV itself. This software and service is available for $52 per user per year with a one time set up fee or $25 per device. The advantage of the per user fee is, if a user has both a desktop and a laptop, both will be covered for the $52 per year.</p>
    <h2 class="section-title">Managed Software Patching</h2>
    <p class="body-text">Keeping computers up-to-date with all critical security patches is an important component in protecting your infrastructure. An effective Patch Management strategy requires timely application of patches. Our patching functions in a closed loop environment. We push the necessary patches to the computers and then use our monitoring system at the device level to verify all have been successfully applied.</p>
    <p class="body-text" style="margin-top:11px">This solution is quite effective for distributed environments with limited local cyber security expertise as well as small offices which prefer to outsource this requirement. Price $3.99 per month per computer. Requires Computer Security Monitoring.</p>
    <h2 class="section-title">Whole Disk Encryption</h2>
    <p class="body-text">We remotely access your computer and perform whole disk encryption as required by your Broker Dealer. We can also help you select the most appropriate encryption methodology for your specific environment. Pricing from $95 per computer.</p>
    <h2 class="section-title">Computer Security Monitoring</h2>
    <p class="body-text">We monitor the security status of your computer on a daily basis. We detect if any new software was installed and if it appears to be dangerous we contact you to discuss the ramifications. We monitor the security patch levels of key software and compare your status to that required by your BD. If there are security fixes available for your computer, we provide you with the necessary information and help get those applied. We also check the status of your anti-virus and disk encryption to make sure it is within guidelines. Pricing $8 per computer per month.</p>
    <h2 class="section-title">New Computer Sourcing</h2>
    <p class="body-text">We are an authorized Veltrix Value Added Reseller and will be happy to help you get your new computer. We work with you to determine an appropriate configuration and what would be a good fit for your specific needs.</p>
  </section>

  <div class="photo front-photo-tablet" role="img" aria-label="Photo of colleagues reviewing charts on a tablet"></div>

  <footer class="contact-bar">
    <div class="photo contact-photo" role="img" aria-label="Photo of hands holding a smartphone"></div>
    <div class="company-block">
      <strong>Keystone Shield LLC</strong>
      P.O. Box 4821 Cedar Bend,<br>TX 78000 US
    </div>
    <div class="reach-block">
      Phone: (555) 010-4417<br>
      Email: info@keystoneshield.com
    </div>
  </footer>
</article>

<article class="page page--back">
  <div class="photo back-photo-growth" role="img" aria-label="Photo of a seedling growing from stacks of coins beside a hand touching rising financial chart graphics"></div>

  <section class="config-column">
    <h2 class="section-title">New Computer Configuration</h2>
    <p class="body-text" style="text-align:left">Configuration services provided for new computers. These can be sourced from us or locally and shipped to us or done remotely. Price $300.</p>
    <h3 class="subhead">Configure for Broker Dealer security requirements</h3>
    <ul>
      <li>Encrypt the Drive</li>
      <li>Set password Policy</li>
      <li>Set Screen saver timeout policy</li>
      <li>Apply all Operating System patches</li>
      <li>Set computer for Auto-update of all products where possible <small>(if not subscribing to our Managed Software Patching service)</small></li>
      <li>Install default Anti-Virus software and configure to policy requirements <small>(if not subscribing to our Managed Anti-Virus service)</small></li>
    </ul>
    <h3 class="subhead">Configure for functionality</h3>
    <ul>
      <li>Remove any unneeded software</li>
      <li>Configure browsers to function most reliably with BD sites</li>
      <li>Remove any unneeded Browser Plug-ins or Tool Bars</li>
      <li>Install Javelin Runtime (as required)</li>
      <li>Install Paperleaf Reader</li>
      <li>Install Quillsuite Office if needed – We can provide Office for $199</li>
    </ul>
    <h3 class="subhead">Safety</h3>
    <ul>
      <li>Create a System Image to an external encrypted drive</li>
      <li>Create Encryption Recovery media and keys if applicable</li>
    </ul>
  </section>

  <div class="photo back-photo-trading" role="img" aria-label="Photo of an analyst working at a desk with multiple market data monitors"></div>
  <div class="photo back-photo-tablet" role="img" aria-label="Photo collage of financial charts on screens and a tablet"></div>

  <section class="service-box box-support">
    <h2 class="section-title">General Computer Support</h2>
    <p class="body-text">Keystone Shield has a long history of working with thousands of Independent Financial Advisors and Broker Dealers across the country. Because of this we have a lot of experience in supporting their technology needs. A benefit of this is we not only understand the technology but also the special needs of the financial services industry. We also understand your security requirements and will execute appropriate non-disclosure agreements to help you insure your information remains private. We've found we can resolve most software and configuration issues remotely. Our rates are $95 per hour.</p>
  </section>
  <section class="service-box box-awareness">
    <h2 class="section-title">Security Awareness Training</h2>
    <p class="body-text">Security Awareness Training is a critical component of a comprehensive cyber security program. Because the cyber security environment is continuously changing, it is our experience that a multi-level approach is most effective in providing timely, actionable information as well as a firm grasp of critical security principals and requirements.</p>
    <p class="body-text">Our first level is a targeted, electronic delivery of mini-training modules, typically taking no longer than 10 minutes to complete, every 4-6 weeks. These short, topical modules are designed to highlight current attacks and the appropriate response to the illustrated threat. The attacks are explained in an easy-to-understand format with the amount of technical jargon kept to the bare minimum. Each module presents several multiple choice questions to insure the respondent has a firm grasp of the topic.</p>
  </section>
  <section class="service-box box-filtering">
    <h2 class="section-title">Internet Blocking and Filtering</h2>
    <p class="body-text">Comprehensive security for your network through award-winning phishing, botnet and malware site protection. Our web filtering service delivers network security services through the DNS layer blocking known malicious or infected sites from resolving on your network. This also allows you to block specific web sites and also broad categories of content from being accessed from your locations. A couple of examples might be Gambling and Pornography. $3.50 per month per device.</p>
  </section>
  <section class="service-box box-firewall">
    <h2 class="section-title">Firewall Sales</h2>
    <p class="body-text">We provide pre-purchase consulting, configuration and support for business grade firewalls. We will help you spec an appropriate firewall, determine if VPN access is needed as well as any dedicated guest Wireless Access. The most suitable device for your location as well as any satellite locations is dependent on organization size and complexity. Prices starting at $750.</p>
  </section>
  <section class="service-box box-ip">
    <h2 class="section-title">Public IP Monitoring</h2>
    <p class="body-text">Knowing what the world sees of your front door to the internet is important. Our Public IP Monitoring scans your static IP address daily looking for inappropriate ports being made available over the internet. If we find your device has changes made we contact you to verify the changes were intentional and explain the ramifications of the changes.</p>
  </section>
</article>

</body>
</html>
```